Creative & Professional Business Card for hair salon

We are looking to update our business cards. Our salon is creative, modern, progressive and professional and looking for a design that will reflect this.

```html
<!DOCTYPE html>
<html lang="en">
<head>
<meta charset="utf-8">
<title>Silver Lining Studio – Business Card</title>
<link href="https://fonts.googleapis.com/css2?family=Roboto+Condensed:wght@300;400&display=swap" rel="stylesheet">
<style>
  :root {
    --backdrop: #dcdcde;
    --card-deep: #15142a;
    --card-mid: #24223f;
    --ink: #f2f2f6;
    --ink-soft: #c9cde0;
    --rule: #8d8fa6;
    --photo-a: #3a3550;
    --photo-b: #6b5a5e;
    --photo-c: #1f1d33;
  }
  * { margin: 0; padding: 0; box-sizing: border-box; }
  html, body { width: 1200px; height: 1200px; overflow: hidden; }
  body {
    background: var(--backdrop);
    font-family: "Roboto Condensed", "Arial Narrow", sans-serif;
    color: var(--ink);
    display: flex;
    align-items: center;
    justify-content: center;
    gap: 60px;
  }
  .card {
    position: relative;
    width: 420px;
    height: 690px;
    background: linear-gradient(160deg, var(--card-mid) 0%, var(--card-deep) 70%);
    box-shadow: 0 18px 40px rgba(0,0,0,0.25);
    overflow: hidden;
  }
  .card__photo {
    position: absolute;
    inset: 0 0 auto 0;
    height: 330px;
    background:
      radial-gradient(ellipse at 55% 45%, var(--photo-b) 0%, var(--photo-a) 40%, var(--photo-c) 80%);
    clip-path: polygon(0 0, 100% 0, 100% 62%, 0 100%);
  }
  .divider {
    position: absolute;
    left: 50px;
    right: 50px;
    display: flex;
    align-items: center;
    gap: 14px;
  }
  .divider::before, .divider::after {
    content: "";
    flex: 1;
    height: 1px;
    background: var(--rule);
  }
  .divider svg { width: 22px; height: 30px; }
  .rule {
    position: absolute;
    left: 50px;
    right: 50px;
    height: 1px;
    background: var(--rule);
  }
  .brand {
    position: absolute;
    left: 0; right: 0;
    text-align: center;
    font-weight: 300;
    color: var(--ink-soft);
    line-height: 1.1;
  }
  .brand__dot {
    display: inline-block;
    width: 14px; height: 14px;
    border-radius: 50%;
    background: var(--ink-soft);
    margin-right: 10px;
    vertical-align: middle;
  }
  .brand__name { font-size: 34px; display: block; }
  .brand__by { font-size: 18px; display: block; margin-top: 4px; }

  .front .divider { top: 415px; }
  .front .brand { top: 490px; }

  .back .appointment {
    position: absolute;
    top: 48px; left: 0; right: 0;
    text-align: center;
    font-size: 21px;
    letter-spacing: 0.5px;
  }
  .back .rule--top { top: 150px; }
  .back .rule--mid { top: 205px; }
  .back .brand { top: 245px; color: var(--ink); }
  .back .brand__dot { background: var(--ink); }
  .back .divider { top: 360px; }
  .contact {
    position: absolute;
    top: 435px; left: 0; right: 0;
    text-align: center;
  }
  .contact__phone { font-size: 42px; letter-spacing: 1px; }
  .contact__handle { font-size: 19px; margin-top: 4px; }
  .contact__web, .contact__email { font-size: 18px; }
  .contact__web { margin-top: 22px; }
  .contact__address { font-size: 18px; margin-top: 18px; }
</style>
</head>
<body>
  <article class="card front">
    <div class="card__photo" role="img" aria-label="Portrait photograph of a model with long softly coloured hair"></div>
    <div class="divider">
      <svg viewBox="0 0 22 30" aria-hidden="true">
        <g fill="none" stroke="#f2f2f6" stroke-width="2">
          <line x1="5" y1="2" x2="15" y2="20"/>
          <line x1="17" y1="2" x2="7" y2="20"/>
          <circle cx="6" cy="24" r="4"/>
          <circle cx="16" cy="24" r="4"/>
        </g>
      </svg>
    </div>
    <div class="brand">
      <span class="brand__name"><span class="brand__dot"></span>Silver Lining Studio</span>
      <span class="brand__by">by Mara Vell</span>
    </div>
  </article>

  <article class="card back">
    <p class="appointment">YOUR NEXT APPOINTMENT IS</p>
    <div class="rule rule--top"></div>
    <div class="brand">
      <span class="brand__name"><span class="brand__dot"></span>Silver Lining Studio</span>
      <span class="brand__by">by Mara Vell</span>
    </div>
    <div class="divider">
      <svg viewBox="0 0 22 30" aria-hidden="true">
        <g fill="none" stroke="#f2f2f6" stroke-width="2">
          <line x1="5" y1="2" x2="15" y2="20"/>
          <line x1="17" y1="2" x2="7" y2="20"/>
          <circle cx="6" cy="24" r="4"/>
          <circle cx="16" cy="24" r="4"/>
        </g>
      </svg>
    </div>
    <div class="contact">
      <p class="contact__phone">07 5000 1234</p>
      <p class="contact__handle">silverLiningbyMaraVell</p>
      <p class="contact__web">www.silverliningstudio.com.au</p>
      <p class="contact__email">salon@silverliningstudio.com.au</p>
      <p class="contact__address">5/12 Harbour Lane, Maroochy</p>
    </div>
  </article>
</body>
</html>
```